Faithful in the Small...Powerful together

Capital Campaign for Brightwell Chapel...need it engaging..spiritually based with pics of the community etc...

Target Market(s)

church congregation and sphere of influence

Industry/Entity Type

religious

Colors
EB3D1F
EC4F4E
F09395
F8D3D4
FCEDEE

Requirements
Must have
• tier levels..engaging scripture and photos

```html
<!DOCTYPE html>
<html lang="en">
<head>
<meta charset="utf-8">
<title>Faithful in the Small, Powerful Together | Brightwell Chapel</title>
<link rel="stylesheet" href="https://fonts.googleapis.com/css2?family=Montserrat:wght@400;600;700&family=Poppins:wght@300;400;500;600&family=Great+Vibes&display=swap">
<style>
  :root {
    --red: #EB3D1F;
    --rose: #EC4F4E;
    --blush: #F09395;
    --pink: #F8D3D4;
    --mist: #FCEDEE;
    --ink: #1f1f1f;
    --body: #3a3a3a;
    --panel: #f2f2f4;
    --night: #050505;
    --rule: #bdbdbd;
  }
  * { margin: 0; padding: 0; box-sizing: border-box; }
  html, body { width: 1200px; height: 927px; overflow: hidden; background: #fff; }
  body { font-family: "Poppins", sans-serif; color: var(--ink); position: relative; }

  .photo { position: absolute; }
  .photo--church { left: 0; top: 0; width: 229px; height: 858px;
    background: linear-gradient(180deg, #4a78c4 0%, #8fb0de 22%, #a55a48 45%, #e9e9ea 65%, #7a6a4f 88%, #5e5340 100%); }
  .photo--speaker { left: 602px; top: 0; width: 180px; height: 381px;
    background: linear-gradient(180deg, #5a5a5a, #9a9a9a 55%, #6b6b6b); }
  .photo--volunteers { left: 786px; top: 0; width: 180px; height: 381px;
    background: linear-gradient(180deg, #d4d4d4, #a9a9a9 55%, #777); }
  .photo--singer { left: 971px; top: 0; width: 229px; height: 858px;
    background: linear-gradient(160deg, #140c0a 0%, #2b1f1a 45%, #6b5a50 75%, #2a201b 100%); }

  .panel { position: absolute; left: 600px; top: 381px; width: 371px; height: 477px; background: var(--panel); }

  .heading { position: absolute; font-family: "Montserrat", sans-serif; line-height: 1.05; }
  .heading__lead { display: block; font-weight: 400; font-size: 17px; color: var(--ink); }
  .heading__accent { display: block; font-weight: 600; font-size: 17.5px; color: var(--red); }

  .text { position: absolute; font-size: 11.4px; line-height: 14.7px; font-weight: 300; color: var(--body); }

  .vision-card { position: absolute; left: 254px; top: 0; width: 289px; height: 284px;
    background: #fff; box-shadow: 0 10px 10px -8px rgba(0,0,0,.25); }
  .vision-intro { left: 265px; top: 104px; width: 105px; font-size: 11.4px; font-weight: 400; color: var(--ink); }
  .vision-divider { position: absolute; left: 381px; top: 108px; width: 1px; height: 56px; background: #d5d5d5; }
  .motto { position: absolute; left: 398px; top: 104px; font-family: "Great Vibes", cursive; font-size: 18.5px; line-height: 18.5px; color: var(--red); }
  .scripture { position: absolute; left: 265px; top: 178px; width: 256px; height: 80px;
    border: 1px dashed #9a9a9a; border-radius: 6px; padding: 4px 8px; font-size: 8.8px; line-height: 12.3px; color: var(--ink); }
  .scripture p + p { margin-top: 8px; }

  .tiers-intro { left: 654px; top: 457px; width: 270px; font-size: 11.4px; }
  .tiers-label { position: absolute; left: 655px; top: 497px; font-size: 10.2px; font-weight: 600; color: var(--ink); }

  .tier-table { position: absolute; left: 655px; top: 531px; width: 280px; border-collapse: collapse; font-size: 11px; color: var(--ink); }
  .tier-table th { font-family: "Poppins", sans-serif; font-weight: 600; font-size: 11px; height: 44px; border-top: 1px solid var(--rule); border-bottom: 1px solid var(--rule); text-align: center; }
  .tier-table th:first-child, .tier-table td:first-child { text-align: left; }
  .tier-table td { font-weight: 300; height: 47px; line-height: 14.5px; text-align: center; border-bottom: 1px dashed #cfcfcf; }
  .tier-table tbody tr:nth-child(3) td, .tier-table tbody tr:nth-child(4) td { height: 44px; }
  .col-group { width: 72px; } .col-people { width: 48px; } .col-weekly { width: 74px; } .col-yearly { width: 86px; }

  .total { position: absolute; left: 655px; top: 757px; width: 66px; height: 42px;
    background: linear-gradient(90deg, var(--rose), #f08a3c); color: #fff;
    font-family: "Montserrat", sans-serif; font-weight: 700; font-size: 11px; line-height: 14.5px; padding: 6px 0 0 5px; }
  .margin-note { position: absolute; left: 763px; top: 760px; font-size: 7px; line-height: 8.7px; color: var(--body); }
  .margin-note ul { list-style: none; }
  .margin-note li::before { content: ""; display: inline-block; width: 4px; height: 4px; border-radius: 50%; margin-right: 2px; background: var(--rose); vertical-align: 1px; }
  .margin-note li:nth-child(2)::before { background: var(--blush); }
  .margin-note li:nth-child(3)::before { background: #999; }

  .footer { position: absolute; left: 0; top: 858px; width: 1200px; height: 69px; background: var(--night); }
  .cta { position: absolute; top: 14px; display: flex; align-items: center; }
  .cta__title { font-family: "Montserrat", sans-serif; font-weight: 600; font-size: 21.5px; color: var(--red); width: 105px; }
  .cta__copy { color: #fff; font-size: 12px; line-height: 16px; }
  .cta__copy strong { display: block; font-family: "Montserrat", sans-serif; font-weight: 700; font-size: 11px; }
  .cta--left { left: 52px; } .cta--right { left: 652px; }
</style>
</head>
<body>
  <div class="photo photo--church" role="img" aria-label="Brightwell Chapel building with white steeple and a Love Like Him, Live Like Him, Lead Like Him feather flag on the lawn"></div>

  <div class="vision-card"></div>
  <h2 class="heading" style="left:263px;top:52px;"><span class="heading__lead">The Heart</span><span class="heading__accent">of the Vision</span></h2>
  <p class="text vision-intro">We are restoring more than space. We are restoring a church where we</p>
  <div class="vision-divider"></div>
  <p class="motto">Love like Him<br>Live like Him<br>Lead like Him</p>
  <div class="scripture">
    <p>“Whoever is faithful in very little is also faithful in much.”<br>Luke 16:10</p>
    <p>“How good and pleasant it is when God’s people live together in unity.”<br>Psalm 133:1</p>
  </div>

  <h2 class="heading" style="left:263px;top:314px;"><span class="heading__lead">Stories of</span><span class="heading__accent">What God Is Doing</span></h2>
  <p class="text" style="left:263px;top:362px;width:275px;">One Wednesday night, a woman went to visit another church, but they were closed for a break. Instead of turning back, she came here. That unexpected moment became a divine appoint-ment. God brought her to Brightwell. Another couple walked through our doors carrying deep church hurt. From the very first moment, they felt seen, valued, and welcomed. What they found here was not just a service, but a family. This is what we are building together.</p>
  <p class="text" style="left:263px;top:524px;width:275px;">These gifts help build momentum, inspire others, and move the vision forward in powerful ways.</p>

  <h2 class="heading" style="left:263px;top:580px;"><span class="heading__lead">How We Move</span><span class="heading__accent">Forward Together</span></h2>
  <p class="text" style="left:263px;top:626px;width:275px;">We encourage everyone to participate, even one dollar a day matters. Some to give stretch gifts as they are able. A few to provide leadership gifts to help anchor the campaign</p>

  <h2 class="heading" style="left:264px;top:712px;"><span class="heading__lead">A Shared</span><span class="heading__accent">Commitment</span></h2>
  <p class="text" style="left:264px;top:760px;width:275px;">“If each of us gave just $20 a week, we would not only meet our goal, we would exceed it. But this is not about equal giving. It is about equal sacrifice. Some can give more, some less, but together, we can do something powerful.”</p>

  <div class="panel"></div>
  <div class="photo photo--speaker" role="img" aria-label="Pastor speaking to the congregation with a headset microphone"></div>
  <div class="photo photo--volunteers" role="img" aria-label="Two volunteers smiling beside a shopping cart full of donated groceries"></div>
  <div class="photo photo--singer" role="img" aria-label="Worship leader singing into a microphone on a dark stage"></div>

  <h2 class="heading" style="left:654px;top:410px;"><span class="heading__lead">Realistic</span><span class="heading__accent">Participation Model</span></h2>
  <p class="text tiers-intro">Not everyone will give equally—so let’s build a real-world scenario:</p>
  <p class="tiers-label">TIERED GIVING PLAN</p>

  <table class="tier-table">
    <colgroup><col class="col-group"><col class="col-people"><col class="col-weekly"><col class="col-yearly"></colgroup>
    <thead><tr><th>Group</th><th>People</th><th>Weekly Gift</th><th>Yearly Total</th></tr></thead>
    <tbody>
      <tr><td>Leadership<br>Givers</td><td>10</td><td>$100</td><td>$52,000</td></tr>
      <tr><td>Core<br>Givers</td><td>40</td><td>$40</td><td>$83,200</td></tr>
      <tr><td>Consistent<br>Givers</td><td>60</td><td>$20</td><td>$62,400</td></tr>
      <tr><td>Entry<br>Givers</td><td>40</td><td>$10</td><td>$20,800</td></tr>
    </tbody>
  </table>
  <div class="total">Total:<br>$218,400</div>
  <div class="margin-note">
    <p>This exceeds the goal, giving margin for:</p>
    <ul><li>Missed weeks</li><li>Lower participation</li><li>Unexpected needs</li></ul>
  </div>

  <footer class="footer">
    <div class="cta cta--left">
      <span class="cta__title">Join Us</span>
      <p class="cta__copy"><strong>PRAY. LISTEN. STEP FORWARD IN FAITH.</strong>Together, we believe God will do more than we can ask or imagine.</p>
    </div>
    <div class="cta cta--right">
      <span class="cta__title">Join Us</span>
      <p class="cta__copy"><strong>PRAY. LISTEN. STEP FORWARD IN FAITH.</strong>Together, we believe God will do more than we can ask or imagine.</p>
    </div>
  </footer>
</body>
</html>
```